Post card for furniture designer in Boston

looking for a neat design to mail out to customers. post card will have writing/pictures in front and back. on the main front, looking for one to two pictures uploaded to be used in a creative way. the back of the post card will be like any generic post card - line down the middle, a space for the stamp/address, four to five lines on both sides to write addresses as well as any other notes. but get creative on this side too. we want the front to include the following descriptions (descriptions will be separated by quotes)
"Liora’s sleek and modern look has enough edge to spice up any room.
In a new room, you'd want something that's easy enough to adjust
and maneuver because you're always trying to figure out what looks
good where. The Liora design, it is light enough to carry from room
to room and it can easily be formed into a table, a bench or a night stand.
The bamboo plywood is structured together to provide an aesthetically
pleasing feel and visually, it's prismal cubed look will give a room that
modern touch."

"- Featured in 2014 Quill’s first showroom
in Soho, NY and won Panel’s Top Pick Prize

- Nominated as one of Best Designs in
2015 Meridel Global Interiors Expo

- Hand picked by Ruth Calloway of Vistra’s
television show, Gilded Room Makers"

"Dimension - 16” by 16” by 16”
Material - Bamboo, Oak & Walnut
Made in Boston

---------------------------------------------------------------------------------------------------------------
LOGO HERE
torvalumecraft.example - Boston, MA - torvalumecraft@mailbox.example

Target Market(s)

high-end, luxury customers

Industry/Entity Type

Furniture Store

Font styles to use
Serif

Requirements
Must have
• logo, contact information, website, one to two photos
Nice to have
• graphic designs that'll incorporate the photos
Should not have
• n/a

```html
<!DOCTYPE html>
<html lang="en">
<head>
<meta charset="utf-8">
<title>Torvalume Craft Postcard</title>
<link rel="stylesheet" href="https://fonts.googleapis.com/css2?family=Open+Sans:wght@400;600;700&display=swap">
<style>
  :root {
    --page: #e9e9ea;
    --card: #ffffff;
    --orange: #f08a24;
    --gold: #f6ae2d;
    --ink: #2b2f3a;
    --navy: #1e2a44;
    --grey: #6b6e74;
    --rule: #c9cbcf;
    --white: #ffffff;
  }
  * { box-sizing: border-box; margin: 0; padding: 0; }
  html, body { width: 741px; height: 1200px; overflow: hidden; }
  body { background: var(--page); font-family: "Open Sans", Arial, sans-serif; position: relative; }

  .card { position: absolute; left: 20px; width: 701px; background: var(--card); box-shadow: 0 2px 6px rgba(0,0,0,.18); overflow: hidden; }
  .card--front { top: 12px; height: 518px; }
  .card--back { top: 605px; height: 580px; }

  /* front */
  .front-photo { position: absolute; inset: 0 0 78px 0;
    background: linear-gradient(160deg, #6d6a63 0%, #a8a49a 30%, #d9d5cc 55%, #efece6 75%, #c7b8a0 100%); }
  .honours { position: absolute; left: 30px; top: 26px; width: 430px; color: var(--white);
    font-size: 16px; line-height: 1.35; text-shadow: 0 1px 2px rgba(0,0,0,.35); }
  .honours p { margin-bottom: 18px; }
  .specs { position: absolute; right: 26px; top: 372px; color: rgba(255,255,255,.85);
    font-size: 9px; line-height: 1.35; text-align: right; }
  .brand { position: absolute; display: flex; align-items: center; gap: 8px; }
  .brand__mark { width: 16px; height: 16px; background: var(--orange); flex: none; }
  .brand__name { color: var(--orange); font-weight: 700; font-size: 17px; letter-spacing: .5px; }
  .front-brand { left: 0; top: 380px; background: var(--white); padding: 14px 22px; }
  .front-contact { position: absolute; left: 28px; top: 456px; color: var(--grey); font-size: 18px; font-weight: 600; }
  .front-bar { position: absolute; left: 0; right: 150px; bottom: 0; height: 10px; background: var(--gold); }

  /* back */
  .back-photo { position: absolute; left: 0; top: 0; width: 300px; height: 238px;
    background: linear-gradient(150deg, #8a8478 0%, #d8d2c6 45%, #f1ede6 70%, #b89c78 100%); }
  .quote-panel { position: absolute; left: 0; top: 238px; width: 330px; height: 318px; background: var(--gold);
    padding: 16px 18px; color: var(--navy); font-size: 12.5px; line-height: 1.38; }
  .quote-panel p + p { margin-top: 2px; }
  .back-brand { left: 345px; top: 20px; }
  .back-contact { position: absolute; left: 400px; top: 84px; color: var(--grey); font-size: 12.5px; line-height: 1.5; text-align: center; width: 200px; }
  .address-lines { position: absolute; left: 370px; right: 28px; top: 170px; }
  .address-lines span { display: block; height: 44px; border-bottom: 1px solid var(--rule); }
</style>
</head>
<body>

<section class="card card--front">
  <div class="front-photo" role="img" aria-label="Photo of the Liora prismatic cube furniture pieces in a bright white room"></div>
  <div class="honours">
    <p>Featured in 2014 Quill’s first showroom<br>in Soho, NY and won Panel’s Top Pick Prize</p>
    <p>Nominated as one of Best Designs in<br>2015 Meridel Global Interiors Expo</p>
    <p>Hand picked by Ruth Calloway of Vistra’s<br>television show, Gilded Room Makers</p>
  </div>
  <div class="specs">
    Dimension - 16” by 16” by 16”<br>
    Material - Bamboo, Oak &amp; Walnut<br>
    Made in Boston
  </div>
  <div class="brand front-brand">
    <span class="brand__mark"></span>
    <span class="brand__name">TORVALUME CRAFT</span>
  </div>
  <p class="front-contact">torvalumecraft.example - Boston, MA - torvalumecraft@mailbox.example</p>
  <div class="front-bar"></div>
</section>

<section class="card card--back">
  <div class="back-photo" role="img" aria-label="Close-up photo of the Liora plywood cube with walnut inlays"></div>
  <div class="quote-panel">
    <p>“Liora’s sleek and modern look has enough edge to spice up any room.</p>
    <p>In a new room, you'd want something that's easy enough to adjust and maneuver because you're always trying to figure out what looks good where.</p>
    <p>The Liora design, it is light enough to carry from room to room and it can easily be formed into a table, a bench or a night stand.</p>
    <p>The bamboo plywood is structured together to provide an aesthetically pleasing feel and visually, it's prismal cubed look will give a room that modern touch.”</p>
  </div>
  <div class="brand back-brand">
    <span class="brand__mark"></span>
    <span class="brand__name">TORVALUME CRAFT</span>
  </div>
  <div class="back-contact">
    torvalumecraft.example<br>- Boston, MA -<br>torvalumecraft@mailbox.example
  </div>
  <div class="address-lines">
    <span></span><span></span><span></span><span></span><span></span>
  </div>
</section>

</body>
</html>
```